Maple Dawn Confections. We need a website as delcious as our chocolate.

I need a website to promote our humble chocolate business. We our proud of are chocolate because we use only our favorite ingredients. We believe in originality and complete enjoyment of our chocolates. I am looking for a sleek and smooth website. I would like to see typical pages such as contact information and an intro. I would like to have a product page, which can be easily updated with photos of new chocolate. I would also like to see a page where we can educate customers about chocolate. This might be tricky but I would like our customers to leave the site knowing they are getting great chocolate! I have a logo and general color scheme, which I will try to upload somewhere. I looking for an original and exciting website.
Updates

Websites we like:

1. http://www.corvel-amand.example/ (looks really good)

2. http://www.tilvarocacao.example/

uploaded logo !

Target Market(s)

People who enjoy chocolate.

Industry/Entity Type

Business

Requirements
Must have
• User Friendly
Page were pictures of new chocolate can be easily updated.

Nice to have
• Calming and appetizing music
Section where recent tweets can show up on the site.

```html
<!DOCTYPE html>
<html lang="en">
<head>
<meta charset="utf-8">
<title>Maple Dawn Confections</title>
<link href="https://fonts.googleapis.com/css2?family=Great+Vibes&family=Noto+Sans:ital,wght@0,400;0,600;1,400&family=Lato:wght@400&display=swap" rel="stylesheet">
<style>
:root{
  --bg-top:#3e2310;
  --bg-bottom:#4d2d12;
  --panel:#2c170a;
  --panel-edge:#6e4424;
  --ink:#ffffff;
  --cream:#f3e6da;
  --link:#3b8fd0;
  --meta:#7aa9d8;
  --pink:#f7c8ec;
  --pink-glow:#d25cbb;
  --tab:#5a3218;
  --tab-light:#7b4a26;
}
*{box-sizing:border-box;margin:0;padding:0}
html,body{width:1053px;height:1200px;overflow:hidden}
body{
  position:relative;
  background:linear-gradient(180deg,var(--bg-top),var(--bg-bottom));
  font-family:"Noto Sans",sans-serif;color:var(--ink);
}
.abs{position:absolute}
.panel{background:var(--panel);border:1px solid var(--panel-edge);box-shadow:2px 3px 6px rgba(0,0,0,.45)}
.rail{position:absolute;top:492px;height:570px;width:1px;background:rgba(120,75,40,.45)}
.script{font-family:"Great Vibes",cursive}
.brand{left:180px;top:39px;width:253px;height:122px;padding:8px;z-index:2}
.brand-plate{background:#fff;width:100%;height:100%;display:flex;align-items:center;justify-content:center;text-align:center;color:#1a1a1a;font-size:24px;line-height:1.15;font-weight:400}
.main-nav{left:511px;top:39px;width:457px;height:54px;display:flex;align-items:center;justify-content:space-around;padding:0 18px}
.main-nav a,.foot-nav a{color:var(--cream);text-decoration:none;font-family:"Great Vibes",cursive}
.main-nav a{font-size:27px}
.main-nav a.current{color:#fff;text-shadow:0 0 6px var(--pink-glow)}
.hero{left:142px;top:113px;width:825px;height:379px}
.hero-copy{left:46px;top:75px;width:262px;font-size:13px;line-height:14.7px}
.hero-copy p{text-indent:32px}
.slider{left:364px;top:55px;width:413px;height:270px;background:#1d0e05;border-radius:8px;padding:9px;box-shadow:0 0 4px rgba(0,0,0,.6)}
.slide{width:100%;height:100%;background:radial-gradient(ellipse at 55% 55%,#e6c9a6 0%,#b8823f 40%,#6e3d15 100%)}
.dots{left:525px;top:347px;display:flex;gap:13px}
.dots span{width:17px;height:17px;border-radius:50%;background:#5a3318;border:2px solid #8a5a30}
.dots span.on{background:#8b6040}
.features{left:141px;top:525px;width:537px;height:351px}
.feature{position:absolute;top:0;width:260px;height:100%}
.feature-title{position:absolute;top:12px;width:200px;height:34px;background:linear-gradient(180deg,var(--tab-light),var(--tab));border:1px solid #2a1407;box-shadow:2px 2px 4px rgba(0,0,0,.5);font-size:25px;line-height:34px;text-align:center;color:var(--cream)}
.feature-photo{position:absolute;top:58px;width:115px;height:115px;border:1px solid #8a6a60}
.feature-copy{position:absolute;top:201px;width:232px;font-size:13px;line-height:14.7px}
.divider{left:267px;top:28px;width:1px;height:309px;background:#6e4424}
.tweets{left:699px;top:525px;width:267px;height:351px}
.tweet-box{position:absolute;left:10px;top:9px;width:247px;height:331px;background:#fff;color:#222;font-size:11px;line-height:12.2px;overflow:hidden}
.tweet-head{height:26px;padding:4px 7px;font-weight:600;font-size:16px;color:var(--link)}
.tweet-list{position:absolute;left:6px;top:32px;width:218px;bottom:2px;overflow:hidden}
.tweet{display:flex;gap:5px;padding:2px 0 4px;border-bottom:1px dotted #ccc}
.tweet .pic{flex:none;width:46px;height:46px;border:1px solid #ccc;background:#a9a9a9}
.tweet .u,.tweet .l{color:var(--link)}
.tweet .m{color:var(--meta);font-style:italic}
.tweet .m b{font-weight:400;color:#bbb}
.scroll{position:absolute;right:4px;top:32px;width:13px;height:295px;background:#e4ecf6;border:1px solid #a8c0de}
.scroll i{position:absolute;left:1px;top:14px;width:9px;height:240px;background:#c8d8ee;border-radius:2px}
.quote{left:141px;top:900px;width:286px;height:137px;padding:20px 20px 0 14px;font-size:11.5px;line-height:12.8px;font-style:italic}
.quote p{text-indent:32px}
.quote cite{display:block;text-align:right;font-size:13px;margin-top:12px}
.slogan{font-family:"Great Vibes",cursive;font-size:36px;color:#3a1a10;text-shadow:0 0 2px var(--pink),0 0 5px var(--pink-glow),0 0 8px var(--pink-glow);white-space:nowrap}
.heart{left:838px;top:895px;width:97px;height:140px;background:radial-gradient(ellipse at 50% 35%,#5c3318 0%,#3a1e0c 55%,rgba(60,32,14,0) 75%)}
.footer{left:142px;top:1060px;width:824px;height:57px}
.copyright{left:13px;top:12px;font-family:"Lato",sans-serif;font-size:12.5px;line-height:15px}
.foot-nav{right:30px;top:13px;display:flex;gap:32px}
.foot-nav a{font-size:21px}
.social{left:811px;top:1127px;display:flex;gap:7px}
.social span{width:26px;height:26px;border-radius:4px;box-shadow:1px 2px 3px rgba(0,0,0,.5)}
</style>
</head>
<body>
<div class="rail" style="left:161px"></div>
<div class="rail" style="left:950px"></div>

<div class="abs panel hero">
  <div class="abs hero-copy">
    <p>Lorem ipsum dolor sit amet, consectetur adipisicing elit, sed do eiusmod tempor incididunt ut labore et dolore magna aliqua. Ut enim ad minim veniam, quis nostrud exercitation ullamco laboris nisi ut aliquip ex ea commodo consequat. Duis aute irure dolor in reprehenderit in voluptate velit esse cillum dolore eu fugiat nulla pariatur.</p>
    <p>Lorem ipsum dolor sit amet, consectetur adipisicing elit, sed do eiusmod tempor incididunt ut labore et dolore magna aliqua. Ut enim ad minim veniam, quis nostrud exercitation ullamco laboris nisi ut aliquip ex ea commodo consequat.</p>
  </div>
  <div class="abs slider"><div class="slide" role="img" aria-label="Photo of a chocolate gift wrapped in cellophane with a ribbon"></div></div>
  <div class="abs dots"><span class="on"></span><span></span><span></span><span></span></div>
</div>

<div class="abs panel brand"><div class="brand-plate">Maple Dawn<br>Confections</div></div>

<nav class="abs panel main-nav">
  <a class="current" href="#">Home</a><a href="#">About</a><a href="#">Gallery</a><a href="#">Contact</a>
</nav>

<section class="abs panel features">
  <div class="feature" style="left:0">
    <div class="feature-title script" style="left:28px">Featured Product</div>
    <div class="feature-photo" style="left:71px;background:linear-gradient(180deg,#e8c9d6 0%,#c79fb4 60%,#7a4a3a 100%)" role="img" aria-label="Photo of chocolates on a display tray"></div>
    <p class="feature-copy" style="left:22px">Lorem ipsum dolor sit amet, consectetur adipisicing elit, sed do eiusmod tempor incididunt ut labore et dolore magna aliqua. Ut enim ad minim veniam, quis nostrud exercitation ullamco laboris nisi ut aliquip ex ea commodo consequat. dolore eu fugiat nulla pariatur.</p>
  </div>
  <div class="abs divider"></div>
  <div class="feature" style="left:275px">
    <div class="feature-title script" style="left:32px">Featured Product</div>
    <div class="feature-photo" style="left:72px;background:radial-gradient(circle at 50% 50%,#6a2a3a 0%,#4a1a24 50%,#c9a0b8 100%)" role="img" aria-label="Photo of truffles in paper cups"></div>
    <p class="feature-copy" style="left:19px">Lorem ipsum dolor sit amet, consectetur adipisicing elit, sed do eiusmod tempor incididunt ut labore et dolore magna aliqua. Ut enim ad minim veniam, quis nostrud exercitation ullamco laboris nisi ut aliquip ex ea commodo consequat. dolore eu fugiat nulla pariatur.</p>
  </div>
</section>

<aside class="abs panel tweets">
  <div class="tweet-box">
    <div class="tweet-head">Chirpline</div>
    <div class="tweet-list">
      <div class="tweet"><span class="pic" role="img" aria-label="Profile photo"></span><div><span class="u">cocoabeanfan</span>: RT <span class="l">@mirabelle_t</span>: Check Chirpline for Bargains - DailyLedger.example <span class="l">http://lnk.example/a6PpU #chirp #bargains</span><br><span class="m">41 seconds ago <b>from</b> Chatterly</span></div></div>
      <div class="tweet"><span class="pic" role="img" aria-label="Profile photo"></span><div><span class="u">hollisgray</span>: <span class="l">#chirp</span> mit <span class="l">#flock</span><br><span class="m">1 minute ago <b>from</b> web</span></div></div>
      <div class="tweet"><span class="pic" role="img" aria-label="Profile photo"></span><div><span class="u">quillmarsh</span>: Just installed ChirpBox - Now I can Chirp directly from Mailroom... <span class="l">http://lnk.example/37NEw8 #mailroom #chirp #plugin</span><br><span class="m">1 minute ago <b>from</b> lnk.example</span></div></div>
      <div class="tweet"><span class="pic" role="img" aria-label="Profile photo"></span><div><span class="u">BrightBizNotes</span>: RT <span class="l">@DorianPlatt</span>: 9 Tips to Build Your Reputation on Chirpline Like <span class="l">@renwestbrook</span> <span class="l">http://short.example/mgtqum #chirp #marketing #pr #branding</span><br><span class="m">2 minutes ago <b>from</b> PostPanel</span></div></div>
    </div>
    <div class="scroll"><i></i></div>
  </div>
</aside>

<blockquote class="abs panel quote">
  <p>“Lorem ipsum dolor sit amet, consectetur adipisicing elit, sed do eiusmod tempor incididunt ut labore et dolore magna aliqua. Ut enim ad minim veniam, quis nostrud exercitation ullamco laboris nisi ut aliquiptur.”</p>
  <cite>-John Smith</cite>
</blockquote>

<div class="abs slogan" style="left:507px;top:896px">Slogan</div>
<div class="abs slogan" style="left:540px;top:943px">Delicious Chocolate,</div>
<div class="abs slogan" style="left:604px;top:990px">Tasty Treats!</div>
<div class="abs heart" role="img" aria-label="Chocolate heart illustration"></div>

<footer class="abs panel footer">
  <div class="abs copyright">Copyright ©2012 Maple Dawn Confections<br>All Rights Reserved</div>
  <nav class="abs foot-nav"><a href="#">Home</a><a href="#">About</a><a href="#">Gallery</a><a href="#">Contact</a></nav>
</footer>

<div class="abs social">
  <span style="background:#3b5b98" role="img" aria-label="Friendwall"></span>
  <span style="background:#4fb3d8" role="img" aria-label="Chirpline"></span>
  <span style="background:#8fa6c8" role="img" aria-label="Searchly"></span>
  <span style="background:#e8832a" role="img" aria-label="News feed"></span>
</div>
</body>
</html>
```